12 Meter Banner-Design Lagerhalle
Zielgruppe
Wir errichten neue Elektroanlagen für Einfamilenhäuser und Wohnungen.
Hallo,
wir möchten auf 12 Meter drei Banner spannen um die unschönen Rohre und Kabel zu verdecken. Jeder der drei Banner soll 400cm breit und 160cm hoch werden.
-Banner 1 links: Motivationsspruch groß, mittig - : Wer immer tut, was er schon kann, bleibt immer das, was er schon ist.
- Banner 2 mitte : Komfortzone ( Grafiken habe ich im Anhang von dem Aufbau der Komfortzone ) Toll wäre ein selbst erstelltes Design passend zum Unternehmen / Farben Schriftart etc.
-Banner 3 rechts: Motivationsspruch : Zusammenkommen ist ein Beginn, zusammenbleiben ist ein Fortschritt, zusammenarbeiten ist ein Erfolg.
- Design nach Vorgabe Druckpilot ( Datasheet) erstellen
Gundsätzlich wäre super, wenn alle 3 Designs/ Banner miteinander harmonieren. Alles andere ist der Kreativität überlassen.
Schriftart: Fira Sans / Montserrat
Wir würden uns über eine Zusammenarbeit freuen.
Beste Grüße

```html
<!DOCTYPE html>
<html lang="de">
<head>
<meta charset="utf-8">
<title>Banner Lagerhalle</title>
<link href="https://fonts.googleapis.com/css2?family=Orbitron:wght@500;600&family=Fira+Sans:wght@400&family=Fira+Sans+Condensed:wght@500&display=swap" rel="stylesheet">
<style>
  :root{
    --stage:#575757;
    --brand-blue:#1a96cc;
    --label-navy:#0e5a7a;
    --zone-pink:#f7c9dd;
    --zone-grey:#c4c4c4;
    --zone-sky:#90bde0;
    --white:#ffffff;
    --ink:#1c1c1c;
    --grommet:#9a9a9a;
  }
  html,body{margin:0;padding:0;overflow:hidden}
  body{width:1200px;height:1200px;background:var(--stage);position:relative}
  .banner{position:absolute;width:1134px;height:453px;overflow:hidden}
  .banner--mini{transform:scale(0.3316);transform-origin:top left}
  .banner--blue{background:var(--brand-blue)}
  .banner--white{background:var(--white)}
  .grommets{position:absolute;inset:0}
  .quote{position:absolute;font-family:"Orbitron",sans-serif;font-weight:600;color:var(--white);text-align:center;margin:0}
  .quote--left{left:350px;width:692px;top:60px;font-size:42px;line-height:81px;letter-spacing:1px}
  .quote--right{left:0;width:1134px;top:112px;font-size:34px;line-height:80px;letter-spacing:1px}
  .brand{position:absolute;left:40px;width:290px;top:190px;text-align:center;font-family:"Orbitron",sans-serif;font-weight:600;font-size:34px;line-height:40px;color:var(--white)}
  .brand-dot{position:absolute;left:985px;top:40px;width:80px;height:80px;border:5px solid var(--white);border-radius:50%;box-sizing:border-box}
  .zone{position:absolute;top:0;width:282px;text-align:center}
  .zone-circle{position:absolute;left:29px;top:37px;width:224px;height:224px;border-radius:50%}
  .zone-label{position:absolute;left:28px;top:201px;width:227px;height:36px;background:var(--label-navy);color:var(--white);font-family:"Fira Sans Condensed",sans-serif;font-weight:500;font-size:24px;line-height:37px;letter-spacing:.5px}
  .zone-traits{position:absolute;left:0;width:282px;top:279px;margin:0;padding:0;list-style:none;font-family:"Fira Sans",sans-serif;font-size:20px;line-height:35px;color:var(--ink);letter-spacing:.6px}
  .zone--comfort .zone-circle{background:var(--zone-pink)}
  .zone--fear .zone-circle{background:var(--zone-grey)}
  .zone--learn .zone-circle{background:var(--zone-sky)}
  .zone--growth .zone-circle{background:var(--brand-blue)}
</style>
</head>
<body>

<svg width="0" height="0" style="position:absolute">
  <defs>
    <g id="grommet-light"><circle r="4.5" fill="none" stroke="#bfbfbf" stroke-width="2"/></g>
    <g id="grommet-dark"><circle r="4.5" fill="none" stroke="#7fb8d6" stroke-width="2"/></g>
    <g id="grommet-set-light">
      <rect x="14" y="14" width="1106" height="425" fill="none" stroke="#cfcfcf" stroke-width="1"/>
      <use href="#grommet-light" x="9" y="9"/><use href="#grommet-light" x="148.5" y="9"/><use href="#grommet-light" x="288" y="9"/><use href="#grommet-light" x="427.5" y="9"/><use href="#grommet-light" x="567" y="9"/><use href="#grommet-light" x="706.5" y="9"/><use href="#grommet-light" x="846" y="9"/><use href="#grommet-light" x="985.5" y="9"/><use href="#grommet-light" x="1125" y="9"/>
      <use href="#grommet-light" x="9" y="444"/><use href="#grommet-light" x="148.5" y="444"/><use href="#grommet-light" x="288" y="444"/><use href="#grommet-light" x="427.5" y="444"/><use href="#grommet-light" x="567" y="444"/><use href="#grommet-light" x="706.5" y="444"/><use href="#grommet-light" x="846" y="444"/><use href="#grommet-light" x="985.5" y="444"/><use href="#grommet-light" x="1125" y="444"/>
      <use href="#grommet-light" x="9" y="154"/><use href="#grommet-light" x="9" y="299"/><use href="#grommet-light" x="1125" y="154"/><use href="#grommet-light" x="1125" y="299"/>
    </g>
    <g id="grommet-set-dark">
      <rect x="14" y="14" width="1106" height="425" fill="none" stroke="#5fb0da" stroke-width="1"/>
      <use href="#grommet-dark" x="9" y="9"/><use href="#grommet-dark" x="148.5" y="9"/><use href="#grommet-dark" x="288" y="9"/><use href="#grommet-dark" x="427.5" y="9"/><use href="#grommet-dark" x="567" y="9"/><use href="#grommet-dark" x="706.5" y="9"/><use href="#grommet-dark" x="846" y="9"/><use href="#grommet-dark" x="985.5" y="9"/><use href="#grommet-dark" x="1125" y="9"/>
      <use href="#grommet-dark" x="9" y="444"/><use href="#grommet-dark" x="148.5" y="444"/><use href="#grommet-dark" x="288" y="444"/><use href="#grommet-dark" x="427.5" y="444"/><use href="#grommet-dark" x="567" y="444"/><use href="#grommet-dark" x="706.5" y="444"/><use href="#grommet-dark" x="846" y="444"/><use href="#grommet-dark" x="985.5" y="444"/><use href="#grommet-dark" x="1125" y="444"/>
      <use href="#grommet-dark" x="9" y="154"/><use href="#grommet-dark" x="9" y="299"/><use href="#grommet-dark" x="1125" y="154"/><use href="#grommet-dark" x="1125" y="299"/>
    </g>
  </defs>
</svg>

<!-- Übersicht: drei Banner nebeneinander -->
<section class="banner banner--blue banner--mini" style="left:30px;top:47px">
  <svg class="grommets" viewBox="0 0 1134 453"><use href="#grommet-set-dark"/></svg>
  <div class="brand">Lorenz Elektro</div>
  <p class="quote quote--left">Wer immer tut,<br>was er schon kann,<br>bleibt immer das,<br>was er schon ist.</p>
</section>

<section class="banner banner--white banner--mini" style="left:411px;top:47px">
  <svg class="grommets" viewBox="0 0 1134 453"><use href="#grommet-set-light"/></svg>
  <div class="zone zone--comfort" style="left:1px">
    <div class="zone-circle" role="img" aria-label="Illustration: Sofa"></div>
    <div class="zone-label">KOMFORTZONE</div>
    <ul class="zone-traits"><li>Kontrolle</li><li>Gewohnheit</li><li>Sicherheit</li><li>Routine</li></ul>
  </div>
  <div class="zone zone--fear" style="left:283px">
    <div class="zone-circle" role="img" aria-label="Illustration: ängstlicher Hase im Loch"></div>
    <div class="zone-label">ANGSTZONE</div>
    <ul class="zone-traits"><li>Unsicherheit</li><li>Ablehnung</li><li>Ausreden</li><li>Abbruch</li></ul>
  </div>
  <div class="zone zone--learn" style="left:564px">
    <div class="zone-circle" role="img" aria-label="Illustration: Teleskop auf Stativ"></div>
    <div class="zone-label">LERNZONE</div>
    <ul class="zone-traits"><li>neue Skills</li><li>Erfahrungen</li><li>Selbstvertrauen</li><li>Zonenausbau</li></ul>
  </div>
  <div class="zone zone--growth" style="left:846px">
    <div class="zone-circle" role="img" aria-label="Illustration: Astronaut auf Rakete"></div>
    <div class="zone-label">WACHSTUMSZONE</div>
    <ul class="zone-traits"><li>Zielerreichung</li><li>Sinnfindung</li><li>Selbstsicherheit</li><li>Zufriedenheit</li></ul>
  </div>
</section>

<section class="banner banner--blue banner--mini" style="left:793px;top:47px">
  <svg class="grommets" viewBox="0 0 1134 453"><use href="#grommet-set-dark"/></svg>
  <div class="brand-dot"></div>
  <p class="quote quote--right">Zusammen ist ein Beginn,<br>zusammenbleiben ist ein Fortschritt,<br>zusammenarbeiten ist ein Erfolg</p>
</section>

<!-- Banner Mitte: Zonenmodell -->
<section class="banner banner--white" style="left:32px;top:255px">
  <svg class="grommets" viewBox="0 0 1134 453"><use href="#grommet-set-light"/></svg>
  <div class="zone zone--comfort" style="left:1px">
    <div class="zone-circle" role="img" aria-label="Illustration: Sofa"></div>
    <div class="zone-label">KOMFORTZONE</div>
    <ul class="zone-traits"><li>Kontrolle</li><li>Gewohnheit</li><li>Sicherheit</li><li>Routine</li></ul>
  </div>
  <div class="zone zone--fear" style="left:283px">
    <div class="zone-circle" role="img" aria-label="Illustration: ängstlicher Hase im Loch"></div>
    <div class="zone-label">ANGSTZONE</div>
    <ul class="zone-traits"><li>Unsicherheit</li><li>Ablehnung</li><li>Ausreden</li><li>Abbruch</li></ul>
  </div>
  <div class="zone zone--learn" style="left:564px">
    <div class="zone-circle" role="img" aria-label="Illustration: Teleskop auf Stativ"></div>
    <div class="zone-label">LERNZONE</div>
    <ul class="zone-traits"><li>neue Skills</li><li>Erfahrungen</li><li>Selbstvertrauen</li><li>Zonenausbau</li></ul>
  </div>
  <div class="zone zone--growth" style="left:846px">
    <div class="zone-circle" role="img" aria-label="Illustration: Astronaut auf Rakete"></div>
    <div class="zone-label">WACHSTUMSZONE</div>
    <ul class="zone-traits"><li>Zielerreichung</li><li>Sinnfindung</li><li>Selbstsicherheit</li><li>Zufriedenheit</li></ul>
  </div>
</section>

<!-- Banner links: Motivationsspruch -->
<section class="banner banner--blue" style="left:34px;top:731px">
  <svg class="grommets" viewBox="0 0 1134 453"><use href="#grommet-set-dark"/></svg>
  <div class="brand">Lorenz Elektro</div>
  <p class="quote quote--left">Wer immer tut,<br>was er schon kann,<br>bleibt immer das,<br>was er schon ist.</p>
</section>

</body>
</html>
```